[Green Press + Juice Bar] Digital Menu Boards (2)

We need designs for our digital menu screens. Dimensions are 1080 x 1920 (9:16). Screens are in portrait mode–2 of them. They will be side by side so designs should be cohesive. We'll need the (Adobe) source files to be able to easily edit in the future.

Check out our Instagram (@pulpwell) to see current brand imagery for inspiration. Please disregard our current website design as it shows our old branding. Visit our Tastemap page to get a feel of the store flow in which the menu boards will be displayed: https://www.tastemap.example/biz/pulpwell-chicago-6

See "Larkfield Menu" attachment for content that will be incorporated into the design for 2 screens.

See "Cleanse Brochure" attachment to see current material we are using to promote our cleansing program. We would like to designate a portion of our menu to promote cleanse options, depending on how much room is available.

Also attached is a photo of our current, static menu board.

We've attached photos of color palettes we like.

Target Market(s)

Health-conscious individuals, healthy moms, fitness gurus, professionals

Industry/Entity Type

Health And Wellness

Font styles to use
Serif
Sans Serif

Colors

Designer to choose colors to be used in the design.

Requirements
Must have
• We need designs for our digital menu screens. Dimensions are 1080 x 1920 (9:16). Screens are in portrait mode–2 of them. We'll need the (Adobe) source files to be able to easily edit in the future. To ensure the sizing of the outputted file is correct and spaced correctly, send us a test file to test on our TV.
Nice to have
• Ideally, the menu will reflect current branding with font usage of one or more of the following:
• FuturaStd-Bold
• Desiderata-Regular
• Wisdom Script
• Bernier Typeface
• Swistblnk Banthers
• Hanley
• If there is space, we'd like to have space to roll a photo/video slideshow on the menu.

```html
<!DOCTYPE html>
<html lang="en">
<head>
<meta charset="utf-8">
<title>Green Press + Juice Bar — Larkfield Menu</title>
<link href="https://fonts.googleapis.com/css2?family=Bebas+Neue&family=Jost:wght@500;600&family=Sail&display=swap" rel="stylesheet">
<style>
  :root {
    --board: #000000;
    --ink: #ffffff;
    --peach: #e9a47b;
    --sage: #a9b87e;
    --mustard: #c8b23c;
    --rule: #9a9a9a;
    --sketch: #262626;
  }
  * { margin: 0; padding: 0; box-sizing: border-box; }
  html, body { width: 675px; height: 1200px; overflow: hidden; background: var(--board); }
  .menu-board {
    position: relative; width: 675px; height: 1200px; overflow: hidden; background: var(--board);
    color: var(--ink); font-family: "Jost", sans-serif; font-weight: 500;
  }
  .block { position: absolute; left: 24px; width: 627px; text-align: center; white-space: normal; }
  .section-title {
    font-family: "Sail", cursive; font-size: 52px; line-height: 60px; font-weight: 400;
  }
  .section-title.bowls { color: var(--peach); }
  .section-title.bites { color: var(--sage); }
  .section-title.soups { color: var(--mustard); }
  .size-tag {
    display: inline-block; font-family: "Bebas Neue", sans-serif; font-size: 20px;
    color: var(--peach); border-top: 2px solid var(--peach); border-bottom: 2px solid var(--peach);
    padding: 0 6px; vertical-align: 14px; margin-left: 8px; line-height: 1.1;
  }
  .swash { display: inline-block; width: 92px; height: 3px; vertical-align: 16px; margin: 0 12px; border-radius: 2px; }
  .bites .swash { background: var(--sage); }
  .soups .swash { background: var(--mustard); }
  .item-name {
    font-family: "Bebas Neue", sans-serif; font-size: 28px; letter-spacing: 1px; line-height: 28px; font-weight: 400;
  }
  .bowl .item-name { color: var(--peach); }
  .bite .item-name { color: var(--sage); }
  .soup .item-name { color: var(--mustard); }
  .price { color: var(--ink); font-size: 22px; letter-spacing: 0.5px; margin-left: 6px; }
  .soup .price { color: var(--mustard); }
  .note { font-size: 17px; margin-left: 8px; letter-spacing: 0.5px; }
  .item-desc { font-size: 14.5px; line-height: 18.5px; padding: 0 8px; }
  .item-desc.airy { line-height: 22px; }
  .label { color: var(--peach); }
  .served { font-family: "Bebas Neue", sans-serif; color: var(--sage); font-size: 17px; line-height: 18px; letter-spacing: 0.5px; }
  .divider {
    position: absolute; left: 209px; width: 257px; height: 5px;
    border-top: 1px solid var(--rule); border-bottom: 1px solid var(--rule);
  }
  .sketch { position: absolute; background: var(--sketch); border-radius: 40%; }
</style>
</head>
<body>
<main class="menu-board">

  <div class="sketch" style="left:36px;top:52px;width:120px;height:52px" role="img" aria-label="Chalk sketch of a whole and halved kiwi"></div>
  <div class="sketch" style="left:534px;top:36px;width:84px;height:68px" role="img" aria-label="Chalk sketch of cherries"></div>
  <div class="sketch" style="left:36px;top:176px;width:84px;height:34px" role="img" aria-label="Chalk sketch of a spinach leaf"></div>
  <div class="sketch" style="left:574px;top:170px;width:76px;height:54px" role="img" aria-label="Chalk sketch of a strawberry"></div>
  <div class="sketch" style="left:84px;top:500px;width:84px;height:40px" role="img" aria-label="Chalk sketch of a kale leaf"></div>
  <div class="sketch" style="left:36px;top:620px;width:68px;height:52px" role="img" aria-label="Chalk sketch of lettuce"></div>
  <div class="sketch" style="left:564px;top:614px;width:68px;height:74px" role="img" aria-label="Chalk sketch of an apple"></div>
  <div class="sketch" style="left:542px;top:752px;width:66px;height:64px" role="img" aria-label="Chalk sketch of a pomegranate"></div>
  <div class="sketch" style="left:36px;top:940px;width:128px;height:56px" role="img" aria-label="Chalk sketch of cashews"></div>
  <div class="sketch" style="left:548px;top:968px;width:68px;height:60px" role="img" aria-label="Chalk sketch of garlic"></div>

  <div class="block" style="top:26px">
    <h1 class="section-title bowls">Bowls<span class="size-tag">20oz</span></h1>
  </div>

  <section class="bowl">
    <h2 class="block item-name" style="top:86px">Matcha Bowl <span class="price">12.5</span></h2>
    <p class="block item-desc" style="top:117px"><span class="label">BASE:</span> Fresh-cracked Coconut Water, Coconut Meat, Banana, Spinach, Medjool Dates, Tocotrienols, Maca, Matcha, Spirulina <span class="label">+ TOPPINGS:</span> Hemp Seeds, Blueberries, Cacao Nibs, Coconut Shreds, Kiwi, Pomegranate Seeds, Banana, Bee Pollen, Mint Sprig</p>
  </section>
  <div class="divider" style="top:184px"></div>

  <section class="bowl">
    <h2 class="block item-name" style="top:196px">Berry Sorcerer <span class="price">12</span></h2>
    <p class="block item-desc" style="top:228px"><span class="label">BASE:</span> Acai, Fresh-pressed Apple Juice, Cherries, Banana, Strawberry, Pomegranate<br><span class="label">+ TOPPINGS:</span> Seasonal Berries, Banana, Sprouted Almond Butter, Coconut Shreds, Goji Berries, Bee Pollen, Housemade Coconut Whip, Housemade Raw Granola, Local Honey</p>
  </section>
  <div class="divider" style="top:290px"></div>

  <section class="bowl">
    <h2 class="block item-name" style="top:301px">Velvet Marmoset <span class="price">12</span></h2>
    <p class="block item-desc" style="top:333px"><span class="label">BASE:</span> Acai, Housemade Almond Milk, Bananas, Blueberries, Peanut Butter, Medjool Dates<br><span class="label">+ TOPPINGS:</span> Housemade Raw Granola, Raw Chocolate Hearts, Peanut Butter, Raw Cacao Drizzle, Banana, Dried Banana Chips, Cacao Nibs, Local Honey, Bee Pollen</p>
  </section>
  <div class="divider" style="top:400px"></div>

  <section class="bowl">
    <h2 class="block item-name" style="top:416px">Keto Bowl <span class="price">13</span><span class="note">*Under 15 Net Carbs*</span></h2>
    <p class="block item-desc" style="top:448px;line-height:19.5px"><span class="label">BASE:</span> Acai, Housemade Almond Milk, Coconut Meat, Avocado, Blueberries, Cauliflower, Pineapple, Sprouted Almond Butter, Xylitol <span class="label">+ TOPPINGS:</span> Seasonal Berries, Coconut Shreds, Bee Pollen, Hemp Seeds, Mulberries, Chia Seeds</p>
  </section>

  <section class="bowl">
    <h2 class="block item-name" style="top:526px">Build Your Own Bowl <span class="price">12.5</span></h2>
    <p class="block item-desc" style="top:558px"><span class="label">STEP 1:</span> Start with Your Liquid: Almond Milk, Apple Juice, Coconut Water<br><span class="label">+ STEP 2:</span> Choose up to 2 fruits/veggies (all bowls include banana) <span class="label">+ STEP 3:</span> Choose up to 2 Superfood Add-ins <span class="label">+ STEP 4:</span> Choose up to 4 Superfood Toppings<br><span class="label">+ STEP 5:</span> Choose a Sweetener (Medjool Dates, Local Honey, Xylitol)</p>
  </section>

  <div class="block bites" style="top:644px">
    <h1 class="section-title bites"><span class="swash"></span>Bites<span class="swash"></span></h1>
  </div>

  <section class="bite">
    <h2 class="block item-name" style="top:708px">Hot Oatmeal + Seasonal Fruit + Superfood Toppings <span class="price">7.5</span></h2>
    <p class="block served" style="top:743px">*Served until 10:30AM*</p>
  </section>
  <div class="divider" style="top:770px"></div>

  <section class="bite">
    <h2 class="block item-name" style="top:784px">Avocado Toast <span class="price">2 Slices: 8.5 * 1 Slice: 4.5</span></h2>
    <p class="block item-desc" style="top:815px">Sprouted Seedhouse 7:2 Bread, Avocado, Pomegranate, Fig, Rosemary</p>
  </section>
  <div class="divider" style="top:840px"></div>

  <section class="bite">
    <h2 class="block item-name" style="top:856px">Orange Cacao Toast <span class="price">2 Slices: 8.5 * 1 Slice: 4.5</span><span class="note">*Seasonal*</span></h2>
    <p class="block item-desc" style="top:887px">Sprouted Seedhouse Cinnamon Raisin Bread, Sprouted Almond Butter, Orange,<br>Cacao Nibs, Local Honey, Basil</p>
  </section>

  <div class="block soups" style="top:946px">
    <h1 class="section-title soups"><span class="swash"></span>Soups<span class="swash"></span></h1>
  </div>

  <section class="soup">
    <h2 class="block item-name" style="top:1016px">Broccoli “Cheddar” Soup <span class="price">16oz</span><span class="note">*Dairy Free*</span></h2>
    <p class="block item-desc airy" style="top:1047px">Red Pepper, Carrot, Cashew, Spring Onion, Lemon, Maple, Nutritional Yeast,<br>Pink Salt, Chili Powder, Garlic Powder, Broccoli</p>
  </section>
  <div class="divider" style="top:1100px"></div>

  <section class="soup">
    <h2 class="block item-name" style="top:1110px">Veggie Soup with Sprouted Lentil <span class="price">16oz</span></h2>
    <p class="block item-desc" style="top:1141px">Leek, Kale, Celery, Red Pepper, Green Onion, Liquid Aminos, Fresh Ginger,<br>Fresh Garlic, Lemon, Salt, Pepper, Cumin, Turmeric, Sprouted Lentils</p>
  </section>

</main>
</body>
</html>
```